Innovation Presentation Template

I need a unique template design for a presentation on Innovation used exclusively inside of our company. I'd prefer to work in Apple Keynote but can take a .ppt and convert it. The template should appeal to a broad audience of diverse job descriptions. This is a one-time presentation that will last between 30 and 45 minutes. The design should provide a strong visual appeal with multiple chart layouts to support highlighted test points (no bullets, I hate bullets), graphics, line art, and video/photos. My presentations are sparse, never more that 2 concepts per chart (usually one). Our company is a high tech manufacturer selling products in many markets ranging from Government to consumer. The final design should include style a style guide including suggested fonts, colors, graph formats, suggested word art, etc.

Target Market(s)

The audience is internal employees only. Strong corporate branding is not required in this presentation.

Industry/Entity Type

Government

Colors
3277b5
faa54b

Requirements
Must have
• Strong visual appeal helping to support the communication of simple concepts (that have been broken down from complex subject matter).

Multiple chart template forms to support different forms of communication including text points, data charts, graphics, photos, and videos.

Visuals will be memorable, but not overpower the content. Visuals will help convey the content.

Well conceived and coordinated color pallets. Fonts guides (that I can access).

You can visit our company web site at www.KOVEX.com to see logo and corporate look/feel. It would be good to build logo into a few of the chart templates, but not all.
Nice to have
• Keynote (please). I can live with .ppt if I have to.

Many charts will make a point with simple single sentences. Find a way to make the sentences graphically interesting by varying font and/or color of specific words to help drive points.

Note that colors that I've identified below are based upon the blue used in our logo and the orange that complements it. I'm not married to these but use them as guidelines.
Should not have
• Noise. Corporate nauseia.

```html
<!DOCTYPE html>
<html lang="en">
<head>
<meta charset="utf-8">
<title>Innovation Presentation Template</title>
<link rel="stylesheet" href="https://fonts.googleapis.com/css2?family=Figtree:ital,wght@0,300;0,400;0,600;0,700;0,800;1,700&display=swap">
<style>
  :root {
    --blue: #3277b5;
    --orange: #faa54b;
    --orange-deep: #fba32f;
    --orange-shadow: #c8661a;
    --ink: #1c1c1c;
    --slate: #415268;
    --paper: #f2f2f2;
    --cream: #f7f3e9;
    --brown: #4a2a0c;
    --green: #89c34a;
    --navy-bar: #3f5067;
    --white: #ffffff;
    --light-blue: #a8d3ef;
  }
  * { box-sizing: border-box; margin: 0; padding: 0; }
  html, body { width: 1200px; height: 1012px; overflow: hidden; }
  body { font-family: "Figtree", "Helvetica Neue", Arial, sans-serif; position: relative; background: var(--white); }
  .panel { position: absolute; width: 600px; overflow: hidden; }

  /* Title slide */
  .title-slide { left: 0; top: 0; height: 336px; background: linear-gradient(135deg, #fbb431, var(--orange-deep)); color: var(--white); }
  .title-slide .kicker { position: absolute; left: 37px; top: 90px; font-size: 27px; font-weight: 300; line-height: 25px; letter-spacing: 0.5px; }
  .title-slide .headline { position: absolute; left: 37px; top: 146px; font-size: 29px; font-weight: 800; letter-spacing: 0.5px; }
  .title-slide .hashtag { position: absolute; left: 37px; top: 185px; font-size: 13px; font-weight: 700; color: var(--brown); }
  .title-slide .brand { position: absolute; left: 30px; top: 262px; display: flex; align-items: center; gap: 8px; }
  .title-slide .brand-mark { width: 30px; height: 30px; background: var(--blue); }
  .title-slide .brand-name { font-size: 40px; font-weight: 800; color: var(--blue); line-height: 1; }
  .title-slide .bulb-art { position: absolute; left: 340px; top: 26px; width: 225px; height: 282px; border-radius: 50% 50% 22% 22% / 45% 45% 18% 18%; background: radial-gradient(circle at 50% 40%, #ffffff 0 45%, #f9c86c 46% 100%); }
  .title-slide .date { position: absolute; left: 519px; top: 305px; font-size: 10px; }

  /* Numbered point */
  .point-slide { left: 600px; top: 0; height: 336px; background: var(--ink); color: var(--white); text-align: center; }
  .point-slide .number { position: absolute; left: 268px; top: 101px; width: 64px; height: 64px; border-radius: 50%; background: var(--orange-deep); font-size: 30px; font-weight: 700; line-height: 64px; }
  .point-slide .statement { position: absolute; left: 0; width: 600px; top: 184px; font-size: 22px; line-height: 27px; font-weight: 400; }
  .point-slide .statement strong { font-weight: 700; }

  /* Text points */
  .text-slide { left: 0; top: 336px; height: 337px; background: linear-gradient(90deg, #ffffff, var(--paper)); }
  .text-slide .photo { position: absolute; left: 0; top: 125px; width: 265px; height: 212px; background: radial-gradient(ellipse at 45% 55%, #cfcfcf, #8a8a8a 55%, #ededed 75%); }
  .text-slide .points { position: absolute; right: 18px; top: 26px; width: 440px; text-align: right; color: var(--ink); }
  .text-slide .point { margin-bottom: 17px; }
  .text-slide h3 { font-size: 16.5px; font-weight: 700; line-height: 21px; }
  .text-slide p { font-size: 13px; line-height: 16px; margin-top: 6px; }
  .text-slide .arrow { display: inline-block; vertical-align: -1px; margin-right: 14px; }
  .text-slide .hl { color: var(--blue); font-weight: 600; }
  .text-slide .hl-bold { color: var(--blue); font-weight: 800; }

  /* Concept diagram */
  .concept-slide { left: 600px; top: 336px; height: 337px; background: var(--slate); color: var(--white); }
  .concept-slide h2 { position: absolute; left: 28px; top: 82px; width: 290px; font-size: 20.5px; line-height: 22px; font-weight: 700; color: var(--orange); }
  .concept-slide p { position: absolute; left: 28px; top: 166px; width: 270px; font-size: 13px; line-height: 18px; }
  .concept-slide em { color: var(--light-blue); font-weight: 700; }
  .concept-slide svg { position: absolute; left: 0; top: 0; }
  .concept-slide .node-label { font-family: "Figtree", sans-serif; font-size: 13.5px; font-weight: 700; fill: var(--white); text-anchor: middle; }

  /* Chart */
  .chart-slide { left: 0; top: 673px; height: 339px; background: var(--cream); }
  .chart-slide h2 { position: absolute; left: 0; width: 600px; top: 30px; text-align: center; font-size: 19.5px; line-height: 22px; font-weight: 700; color: var(--brown); }
  .chart-slide svg { position: absolute; left: 0; top: 0; }
  .chart-slide .bar-value { font-family: "Figtree", sans-serif; font-size: 23px; font-weight: 700; fill: var(--white); text-anchor: middle; }
  .chart-slide .bar-label { font-family: "Figtree", sans-serif; font-size: 13.5px; fill: #333333; text-anchor: middle; }

  /* Quote */
  .quote-slide { left: 600px; top: 673px; height: 339px; background: var(--orange-deep); color: var(--white); }
  .quote-slide blockquote { position: absolute; left: 83px; top: 80px; width: 500px; font-size: 23px; line-height: 28.2px; font-weight: 300; }
  .quote-slide blockquote strong { font-weight: 700; }
  .quote-slide .mark { position: absolute; font-size: 96px; font-weight: 800; color: var(--orange-shadow); line-height: 1; font-family: Georgia, serif; }
  .quote-slide .mark.open { left: 33px; top: 64px; }
  .quote-slide .mark.close { left: 505px; top: 242px; }
</style>
</head>
<body>

<section class="panel title-slide">
  <div class="kicker">WHAT DO YOU<br>KNOW ABOUT</div>
  <div class="headline">INNOVATION</div>
  <div class="hashtag">#thinkinnovate</div>
  <div class="bulb-art" role="img" aria-label="Illustration of a light bulb with a brain inside and radiating rays"></div>
  <div class="brand"><span class="brand-mark"></span><span class="brand-name">KOVEX</span></div>
  <div class="date">May 07, 2014</div>
</section>

<section class="panel point-slide">
  <div class="number">1</div>
  <div class="statement"><strong>IT IS A LONG ESTABLISHED</strong><br>FACT THAT A WILL BE DISTRACTED</div>
</section>

<section class="panel text-slide">
  <div class="photo" role="img" aria-label="Black and white photo of a relaxed woman looking upward, hands behind her head"></div>
  <div class="points">
    <div class="point">
      <h3>Mauris ac libero sit amet dui pretium elit fermentum<br>Aliquam eu elit euismod, viverra diam a, tincidunt</h3>
      <p><svg class="arrow" width="12" height="10" viewBox="0 0 12 10"><path d="M2 2 H7 A3 3 0 0 1 7 8 H2" fill="none" stroke="#faa54b" stroke-width="2"/></svg>Etiam convallis augue posuere <span class="hl-bold">1997</span> lorem sollicitudin, rutrum.</p>
    </div>
    <div class="point">
      <h3>Curabitur sollicitudin massa nec lorem<br>gravida, a lacinia risus ultricies.</h3>
      <p><svg class="arrow" width="12" height="10" viewBox="0 0 12 10"><path d="M2 2 H7 A3 3 0 0 1 7 8 H2" fill="none" stroke="#faa54b" stroke-width="2"/></svg>Pellentesque rutrum quam vitae vestibulum.</p>
    </div>
    <div class="point">
      <h3>Etiam convallis augue posuere<br>lorem sollicitudin, sed rutrum<br>turpis ornare.</h3>
      <p><svg class="arrow" width="12" height="10" viewBox="0 0 12 10"><path d="M2 2 H7 A3 3 0 0 1 7 8 H2" fill="none" stroke="#faa54b" stroke-width="2"/></svg>Cras quis <span class="hl">Impact</span> faucibus pulvinar ,<br>pulvinar mi vel, viverra arcu.</p>
    </div>
  </div>
</section>

<section class="panel concept-slide">
  <h2>There are many variations of passages of Lorem Ipsum available.</h2>
  <p>The majority have suffered alteration in some form, by injected humour, or randomised words which don't look even <em>slightly believable</em>. If you are going to use a passage.</p>
  <svg width="600" height="337" viewBox="0 0 600 337">
    <circle cx="443" cy="176" r="92" fill="none" stroke="#c9d1db" stroke-width="1"/>
    <circle cx="443" cy="100" r="57" fill="#ffffff"/>
    <circle cx="443" cy="100" r="50" fill="#faa54b"/>
    <text class="node-label" x="443" y="104">recognition</text>
    <circle cx="370" cy="214" r="57" fill="#ffffff"/>
    <circle cx="370" cy="214" r="50" fill="#3277b5"/>
    <text class="node-label" x="370" y="218">commit</text>
    <circle cx="512" cy="214" r="57" fill="#ffffff"/>
    <circle cx="512" cy="214" r="50" fill="#1c1c1c"/>
    <text class="node-label" x="512" y="218">feel</text>
  </svg>
</section>

<section class="panel chart-slide">
  <h2>All the Lorem Ipsum generators on the Inter-<br>net tend to repeat predefined chunks</h2>
  <svg width="600" height="339" viewBox="0 0 600 339">
    <rect x="80" y="174" width="75" height="100" fill="#faa54b"/>
    <text class="bar-value" x="117" y="203">27%</text>
    <rect x="203" y="110" width="75" height="164" fill="#3277b5"/>
    <text class="bar-value" x="240" y="139">41%</text>
    <rect x="327" y="133" width="75" height="141" fill="#89c34a"/>
    <text class="bar-value" x="364" y="162">36%</text>
    <rect x="451" y="200" width="75" height="74" fill="#3f5067"/>
    <text class="bar-value" x="488" y="229">18%</text>
    <line x1="50" y1="274.5" x2="549" y2="274.5" stroke="#555" stroke-width="1" stroke-dasharray="1 1.5"/>
    <text class="bar-label" x="116" y="303">The Internet</text>
    <text class="bar-label" x="239" y="303">Repeat predefined</text>
    <text class="bar-label" x="363" y="303">Embarrassing</text>
    <text class="bar-label" x="487" y="303">5% Chunks</text>
  </svg>
</section>

<section class="panel quote-slide">
  <span class="mark open">&ldquo;</span>
  <blockquote>It is a long established fact that a reader will be distracted by the readable con-tent of a page when looking at its layout. The point of using Lorem Ipsum is that it has a more-or-less norma <strong>'Content here, content here', making it look like</strong></blockquote>
  <span class="mark close">&rdquo;</span>
</section>

</body>
</html>
```